new incubator startup Plattform

I need a flyer for a business presentation.
Please insert the text ideas from following the attachment.

We are a new incubator, accelerator and co working space for startups. The innovation platform that unites global companies with high tech expertise and the best of Austrian knowhow. Our focus is in AI, Blockchain and e-commerce.
We are a neutral platform moderating an in-depth and curated collaboration between our partners from the industry and young tech companies. Our network of investment firms and mentors further helps the growth of tech companies. Our home is Vienna, a hub of business, engineering, and groundbreaking inventions.

Focus:
AI, Blockchain, e-commerce

Cases
Startup Idea
You have a disruptive idea that needs an accelerator/incubator program

Business Challenge
You want to solve an business problem but do not own an idea

Mature startup Idea
You Have a Disruptive idea that needs a direct commercialization

Benefits
Market and Investor Acces
Direct access to all Partners

Training and Tools

Mentor and Network Muscle
We can link you to many domains like Sales, Marketing, Aftersales, IT und HR.
Experiences Senior and University mentors.
With all Partners as your first potential customer.

```html
<!DOCTYPE html>
<html lang="en">
<head>
<meta charset="utf-8">
<title>Nordhaus Lab – Startup Flyer</title>
<link href="https://fonts.googleapis.com/css2?family=Open+Sans:wght@400;600;700;800&display=swap" rel="stylesheet">
<style>
  :root{
    --blue:#1b8fd6;
    --blue-dark:#0d5fa3;
    --blue-light:#5cbcf0;
    --ink:#4a4f55;
    --muted:#7b8188;
    --paper:#ffffff;
    --stage:#e9ecef;
  }
  *{box-sizing:border-box;margin:0;padding:0}
  html,body{width:707px;height:1200px;overflow:hidden;background:var(--stage)}
  body{font-family:"Open Sans",Arial,sans-serif;color:var(--ink)}
  .flyer{position:relative;width:707px;height:1200px;background:var(--paper);overflow:hidden}
  .flyer-art{position:absolute;inset:0}
  .brand{position:absolute;left:44px;top:62px;display:flex;align-items:center;gap:14px}
  .brand-mark{width:40px;height:40px;background:var(--blue-dark)}
  .brand-name{font-size:30px;font-weight:700;color:var(--blue-dark);letter-spacing:1px}
  .content{position:absolute;top:668px;left:40px;right:40px;display:grid;grid-template-columns:1fr 1fr;gap:34px}
  .section-title{font-size:17px;font-weight:800;color:var(--blue);text-transform:uppercase;margin-bottom:14px;letter-spacing:.5px}
  .section-title.spaced{margin-top:24px}
  .case{display:flex;gap:12px;margin-bottom:18px;align-items:flex-start}
  .case-icon{flex:0 0 34px;height:38px}
  .case-title{font-size:12.5px;font-weight:700;color:var(--blue);text-transform:uppercase}
  .case-title span{font-weight:400;color:var(--muted)}
  .case-text{font-size:11.5px;line-height:1.45;color:var(--ink);margin-top:2px}
  .bullets{list-style:none}
  .bullets li{position:relative;padding-left:20px;font-size:11.5px;line-height:1.45;margin-bottom:6px}
  .bullets li::before{content:"";position:absolute;left:0;top:4px;width:10px;height:10px;background:var(--blue);clip-path:polygon(25% 0,75% 0,100% 50%,75% 100%,25% 100%,0 50%)}
  .footer{position:absolute;left:44px;bottom:26px;display:flex;align-items:center;gap:10px;color:#fff;font-size:14px;font-weight:600}
  .footer svg{width:16px;height:16px}
</style>
</head>
<body>
<div class="flyer">
  <svg class="flyer-art" width="707" height="1200" viewBox="0 0 707 1200">
    <defs>
      <linearGradient id="portScene" x1="0" y1="0" x2="0" y2="1">
        <stop offset="0" stop-color="#7fa9cf"/>
        <stop offset=".45" stop-color="#5a83ad"/>
        <stop offset=".7" stop-color="#c07a3e"/>
        <stop offset="1" stop-color="#3b3f4a"/>
      </linearGradient>
      <linearGradient id="bandGrad" x1="0" y1="0" x2="1" y2="1">
        <stop offset="0" stop-color="#5cbcf0"/>
        <stop offset="1" stop-color="#0d5fa3"/>
      </linearGradient>
    </defs>
    <!-- top right bands -->
    <polygon points="430,0 707,0 707,250" fill="url(#bandGrad)"/>
    <polygon points="560,0 707,0 707,130" fill="#0d5fa3"/>
    <polygon points="380,0 430,0 707,250 707,290" fill="#d9e6f2"/>
    <!-- port photograph -->
    <polygon role="img" aria-label="Photo of an industrial container port at dusk with cranes" points="0,200 707,200 707,520 0,600" fill="url(#portScene)"/>
    <polygon points="0,170 300,170 240,200 0,200" fill="#1b8fd6"/>
    <!-- slanted band under photo -->
    <polygon points="0,600 707,520 707,560 0,640" fill="url(#bandGrad)"/>
    <polygon points="360,560 707,520 707,600 500,600" fill="#0d5fa3"/>
    <!-- hexagon thumbnails -->
    <g stroke="#ffffff" stroke-width="5">
      <polygon role="img" aria-label="Photo of network server hardware" points="105,475 150,475 173,515 150,555 105,555 82,515" fill="#3f6f96"/>
      <polygon role="img" aria-label="Photo of a shipping yard" points="180,515 225,515 248,555 225,595 180,595 157,555" fill="#6f8aa3"/>
      <polygon role="img" aria-label="Photo of a cargo truck" points="255,475 300,475 323,515 300,555 255,555 232,515" fill="#8aa8c2"/>
      <polygon role="img" aria-label="Photo of stacked containers" points="330,515 375,515 398,555 375,595 330,595 307,555" fill="#b7835a"/>
    </g>
    <!-- footer band -->
    <polygon points="0,1130 707,1090 707,1200 0,1200" fill="url(#bandGrad)"/>
    <polygon points="420,1106 707,1090 707,1200 560,1200" fill="#0d5fa3"/>
  </svg>

  <div class="brand">
    <div class="brand-mark"></div>
    <div class="brand-name">NORDHAUS LAB</div>
  </div>

  <div class="content">
    <section class="cases">
      <h2 class="section-title">Cases</h2>
      <div class="case">
        <svg class="case-icon" viewBox="0 0 34 38"><polygon points="17,1 33,10 33,28 17,37 1,28 1,10" fill="var(--blue)"/><path d="M10 19l5 5 9-10" stroke="#fff" stroke-width="3" fill="none"/></svg>
        <div><div class="case-title">Startup <span>Idea</span></div>
        <p class="case-text">You have a disruptive idea that needs an accelerator/incubator program</p></div>
      </div>
      <div class="case">
        <svg class="case-icon" viewBox="0 0 34 38"><polygon points="17,1 33,10 33,28 17,37 1,28 1,10" fill="var(--blue)"/><path d="M10 19l5 5 9-10" stroke="#fff" stroke-width="3" fill="none"/></svg>
        <div><div class="case-title">Business <span>Challenge</span></div>
        <p class="case-text">You want to solve a business problem but do not own an idea</p></div>
      </div>
      <div class="case">
        <svg class="case-icon" viewBox="0 0 34 38"><polygon points="17,1 33,10 33,28 17,37 1,28 1,10" fill="var(--blue)"/><path d="M10 19l5 5 9-10" stroke="#fff" stroke-width="3" fill="none"/></svg>
        <div><div class="case-title">Mature Startup <span>Idea</span></div>
        <p class="case-text">You have a disruptive idea that needs a direct commercialization</p></div>
      </div>
    </section>

    <section class="benefits">
      <h2 class="section-title">Benefits</h2>
      <ul class="bullets">
        <li>Market and Investor Access</li>
        <li>Direct access to all Partners</li>
      </ul>
      <h2 class="section-title spaced">Training and Tools</h2>
      <ul class="bullets">
        <li>Mentor and Network Muscle</li>
        <li>We can link you to many domains like Sales, Marketing, Aftersales, IT and HR.</li>
        <li>Experienced Senior and University mentors.</li>
        <li>With all Partners as your first potential customer.</li>
      </ul>
    </section>
  </div>

  <div class="footer">
    <svg viewBox="0 0 16 16"><circle cx="8" cy="8" r="7" stroke="#fff" stroke-width="1.5" fill="none"/><path d="M1 8h14M8 1c-3 4-3 10 0 14M8 1c3 4 3 10 0 14" stroke="#fff" stroke-width="1.2" fill="none"/></svg>
    <span>www.nordhauslab.example</span>
    <span>|</span>
    <svg viewBox="0 0 16 16"><path d="M4 1l3 3-2 2c1 2 3 4 5 5l2-2 3 3-2 3C7 15 1 9 1 3z" fill="#fff"/></svg>
    <span>(1) 555-0142</span>
  </div>
</div>
</body>
</html>
```